Detailing informational flyer

I want to design a new flyer for my automotive detailing business. The flyer should use the color scheme from the logo and be easy to read and understand the services we offer.

Industry/Entity Type

Automotive

Font styles to use
Serif
Sans Serif

Colors
3176b5
0255a3
fbed22
33a6d7
0692cd
ffffff

Requirements
Must have
• must include all information from the copy
Nice to have
• include a Glavenor logo such as the image attached

```html
<!DOCTYPE html>
<html lang="en">
<head>
<meta charset="utf-8">
<title>Detail Center Brookvale Carwash – Detailing Services</title>
<link href="https://fonts.googleapis.com/css2?family=Roboto:wght@400;700;900&family=Roboto+Condensed:wght@700&display=swap" rel="stylesheet">
<style>
  :root {
    --navy: #1b2463;
    --navy-deep: #141b4d;
    --sky: #67a1da;
    --royal: #3176b5;
    --yellow: #f4e37c;
    --ink: #1b1f3a;
    --paper-top: #ffffff;
    --paper-bottom: #dcdde2;
    --stage: #d4d5d8;
  }
  * { margin: 0; padding: 0; box-sizing: border-box; }
  html, body { width: 1106px; height: 1200px; overflow: hidden; }
  body { background: var(--stage); font-family: "Roboto", Arial, sans-serif; position: relative; }

  .flyer {
    position: absolute; left: 143px; top: 20px; width: 820px; height: 1160px;
    background: linear-gradient(180deg, var(--paper-top) 50%, var(--paper-bottom) 100%);
    overflow: hidden; box-shadow: 0 4px 14px rgba(0,0,0,.25);
  }
  .flyer-shapes { position: absolute; inset: 0; }

  .brand-mark { position: absolute; left: 31px; top: 60px; width: 291px; text-align: center; }
  .brand-mark .dot { width: 74px; height: 74px; border-radius: 50%; background: var(--yellow); margin: 0 auto 14px; }
  .brand-mark .name {
    font-family: "Roboto Condensed", Arial, sans-serif; font-weight: 700; color: var(--navy);
    font-size: 25px; line-height: 1.15; letter-spacing: 2px; text-transform: uppercase;
  }

  .hero-title {
    position: absolute; left: 55px; top: 330px;
    font-family: "Roboto Condensed", Arial, sans-serif; font-weight: 700;
    color: var(--yellow); font-size: 38px; line-height: 46px; text-transform: uppercase;
  }

  .partner-badge {
    position: absolute; left: 624px; top: 482px; width: 160px; height: 80px;
    display: flex; align-items: center; justify-content: center; gap: 8px;
  }
  .partner-badge .square { width: 14px; height: 14px; background: var(--royal); }
  .partner-badge .name { font-family: "Roboto Condensed", Arial, sans-serif; font-weight: 700; font-size: 28px; color: var(--navy); text-transform: uppercase; }

  .call-to-action {
    position: absolute; left: 0; top: 586px; width: 820px; text-align: center;
    font-family: "Roboto Condensed", Arial, sans-serif; font-weight: 700;
    color: var(--navy); font-size: 30px; line-height: 38px; text-transform: uppercase;
  }

  .service-photo {
    position: absolute; left: 48px; width: 233px; height: 156px;
    border: 2px solid var(--navy); border-radius: 16px;
  }
  .service-photo.engine { top: 677px; background: linear-gradient(135deg, #4a4f57, #9ea3aa 55%, #2b2e34); }
  .service-photo.polish { top: 841px; background: linear-gradient(135deg, #8fa0b3, #1d232c 55%, #c9cfd6); }

  .services { position: absolute; left: 301px; top: 674px; width: 459px; }
  .service { font-size: 13px; line-height: 16.6px; color: #333; text-align: justify; margin-bottom: 14px; }
  .service strong { color: var(--navy); font-weight: 700; font-size: 15px; }

  .headlight-note {
    position: absolute; left: 62px; top: 1070px; width: 400px;
    color: #fff; font-size: 13px; line-height: 16.6px;
  }
  .headlight-note strong { color: var(--sky); font-size: 15px; font-weight: 700; }

  .contact {
    position: absolute; right: 79px; top: 1070px; text-align: right;
    font-weight: 700; font-size: 18px; line-height: 23px; color: var(--navy);
  }
</style>
</head>
<body>
<main class="flyer">
  <svg class="flyer-shapes" width="820" height="1160" viewBox="0 0 820 1160" aria-hidden="true">
    <defs>
      <linearGradient id="topBand" x1="0" x2="1">
        <stop offset="0" stop-color="#1b2463"/><stop offset="1" stop-color="#3f7dc4"/>
      </linearGradient>
      <linearGradient id="heroPanel" x1="0" y1="0" x2="0" y2="1">
        <stop offset="0" stop-color="#2d4a9a"/><stop offset="1" stop-color="#141b4d"/>
      </linearGradient>
    </defs>
    <rect x="0" y="0" width="820" height="600" fill="#141b4d"/>
    <polygon points="0,420 120,330 330,380 820,380 820,600 0,600" fill="url(#heroPanel)"/>
    <rect x="322" y="0" width="498" height="40" fill="url(#topBand)"/>
    <polygon points="322,466 820,466 820,515 360,515" fill="#3f7dc4"/>
    <path d="M0,582 C150,560 300,528 382,520 L820,512 L820,1160 L0,1160 Z" fill="#fbfbfc"/>
    <polygon points="31,0 322,0 322,258 176,290 31,258" fill="#67a1da"/>
    <polygon points="31,270 176,302 322,270 322,278 176,310 31,278" fill="#67a1da"/>
    <polygon points="22,1055 497,1055 480,1158 22,1158" fill="#1b2463"/>
    <polygon points="500,1055 782,1055 782,1158 483,1158" fill="#67a1da"/>
  </svg>

  <div class="service-photo hero" role="img" aria-label="Gloved hand brushing dust from a car dashboard console"
       style="position:absolute;left:322px;top:62px;width:498px;height:404px;border:0;border-radius:0;background:linear-gradient(120deg,#2a2230 0%,#6b4b44 35%,#a9a4a8 60%,#3a3a44 100%);"></div>

  <div class="brand-mark">
    <div class="dot"></div>
    <div class="name">Detail Center<br>Brookvale Carwash</div>
  </div>

  <h1 class="hero-title">Detail<br>Center<br>Brookvale<br>Carwash</h1>

  <div class="partner-badge">
    <span class="square"></span><span class="name">Glavenor</span>
  </div>

  <h2 class="call-to-action">Ask to speak to a manager about<br>scheduling any of our detailing services.</h2>

  <div class="service-photo engine" role="img" aria-label="Hand cleaning a car engine bay with a sponge"></div>
  <div class="service-photo polish" role="img" aria-label="Hand polishing a dark car bonnet beside the headlight"></div>

  <section class="services">
    <p class="service"><strong>Exterior detailing includes:</strong> We wash, clay, compound, polish, and wax, as needed to restore the deep rich gloss and provide a durable shine for that “new car” look. This process removes light oxidation from the vehicle and protects the clear coat finish. Finishing touches include rim cleaning and tire shine.</p>
    <p class="service"><strong>Interior detailing shampoo includes:</strong> We perform a deep cleaning of the interior such as the dashboard, door jams, center console, trunk area, upholstered seats, and all carpets and mats. This process will remove soils and most stains. Windows are cleaned inside and out. All leather is dressed to provide a protective finish. Air freshener is available upon request.</p>
    <p class="service"><strong>Mini detail/ VIP service includes:</strong> Brookvale Special Wash with triple polish wax, Glavenor Shield protectant, tire shine, and a detailed and gentle cleaning of the upholstery. 4 rubber or carpet mats are shampooed. All interior surfaces are dressed including dashboard, door panels, center console. This is followed by a detailed carpet and upholstery vacuum with compressed air to remove dirt from hard to reach places. For added shine ask about adding on our express wax service to your mini detail package.</p>
  </section>

  <p class="headlight-note"><strong>Headlight restoration:</strong> This shop proudly offers the Headlight Service, which can polish or restore your headlight to a clear, safe condition at a fraction of the cost of headlight replacement! Restore the lens to a clear, shiny &amp; safe condition.</p>

  <address class="contact" style="font-style:normal;">418-20 Harbor Ave,<br>Elm Terrace<br>Call +1 555-014-2290</address>
</main>
</body>
</html>
```